Want a DL Flyer designed for mailout, with the following info. Please see the website www.ledgerwise.com.au for any other info.
Content:
EVERYTHING YOU NEED FROM AN ACCOUNTANT
(tick) Value for money
(tick) Mobile visits to your farm or business
(tick) Fixed Fees Agreed Upfront
(tick) Advice tailored to your circumstances
(tick) Help to grow your business
(tick) Talk directly to your accountant, the person who knows you
(tick) Small business & Primary Producer Specialists
+ MORE.......LEDGERWISE. YOU'RE MORE THAN A FILE TO US.
Director: Peter Dunmore CPA | Associate: Belinda Vasey CPA
Call (07) 4619 2235 www.ledgerwise.com.au PO Box 716 Dalby Qld 4405

```html
<!DOCTYPE html>
<html lang="en">
<head>
<meta charset="utf-8">
<title>Ledgerwise DL Flyer</title>
<link href="https://fonts.googleapis.com/css2?family=Rubik:ital,wght@0,400;0,500;0,700;1,700&family=Lato:wght@400;700&display=swap" rel="stylesheet">
<style>
  :root{
    --red:#c8161d;
    --red-dark:#9e0f14;
    --charcoal:#3d3d3d;
    --grey:#5a5a5a;
    --text:#444;
    --white:#fff;
    --page:#d9d9d9;
  }
  *{box-sizing:border-box;margin:0;padding:0}
  html,body{width:1200px;height:902px;overflow:hidden}
  body{background:var(--page);position:relative;font-family:'Lato',sans-serif;color:var(--text)}
  .flyer{position:absolute;top:50px;width:390px;height:801px;overflow:hidden;background:var(--white);box-shadow:0 12px 22px rgba(0,0,0,.28)}
  .flyer--front{left:160px}
  .flyer--back{left:650px}
  .shapes{position:absolute;inset:0;width:390px;height:801px}
  .abs{position:absolute}

  .brand{display:flex;align-items:center;gap:8px;font-family:'Rubik',sans-serif;font-weight:500;color:var(--red)}
  .brand__mark{background:var(--red);display:block}
  .brand--front{left:0;right:0;top:82px;justify-content:center;font-size:31px}
  .brand--front .brand__mark{width:22px;height:22px}

  .headline{left:0;right:0;top:186px;text-align:center;font-family:'Rubik',sans-serif;font-weight:700;color:var(--white);font-size:31px;line-height:42px;letter-spacing:.3px}

  .why{left:31px;top:354px;font-family:'Rubik',sans-serif;font-size:15px;line-height:19px;font-weight:500}
  .why__lead{color:var(--red)}
  .why__name{color:var(--grey)}

  .benefits{left:29px;top:406px;width:310px;list-style:none;font-size:13px;color:var(--text)}
  .benefits li{position:relative;padding-left:26px;line-height:16px;margin-bottom:8px}
  .benefits svg{position:absolute;left:0;top:1px;width:15px;height:14px}

  .slogan{left:0;width:390px;top:597px;text-align:center;font-family:'Rubik',sans-serif;font-style:italic;font-weight:700;font-size:20px;line-height:26px}
  .slogan__name{color:var(--grey);display:block}
  .slogan__line{color:var(--red);display:block}

  .portrait{border-radius:50%;border:3px solid var(--white);box-shadow:0 2px 6px rgba(0,0,0,.3);background:radial-gradient(circle at 50% 40%,#8fa48a,#3f5b3a 70%)}
  .portrait--front{left:263px;top:655px;width:80px;height:80px}
  .portrait--back{left:216px;top:264px;width:140px;height:140px}

  .contact{font-size:10.5px;color:var(--white);line-height:16px}
  .contact--front{left:42px;top:739px}
  .contact__row{display:flex;align-items:center;gap:6px}
  .icon{width:11px;height:11px;flex:none}
  .divider{left:214px;top:741px;width:1px;height:32px;background:var(--white)}
  .staff{left:224px;top:746px;font-size:10px;line-height:14px;color:var(--white)}
  .web--front{left:0;right:0;top:787px;display:flex;justify-content:center;align-items:center;gap:6px;font-size:11px;color:var(--white)}

  .photo--back{left:0;top:0;width:390px;height:250px;background:linear-gradient(160deg,#f3f6fa 0%,#b7c9dd 40%,#4e6f95 75%,#223a5a 100%)}
  .badge{left:30px;top:269px;color:var(--white);font-family:'Rubik',sans-serif}
  .badge__name{font-size:15px;font-weight:500;margin-bottom:6px}
  .badge__meta{font-size:12.5px;font-weight:500;line-height:16px}

  .about{left:31px;top:410px;width:330px;font-size:11.2px;line-height:14.6px;text-align:justify;color:var(--text)}
  .about p{margin-bottom:14.6px}

  .brand--back{left:12px;top:716px;width:140px;flex-direction:column;gap:6px;font-size:17px}
  .brand--back .brand__mark{width:26px;height:26px}
  .contact-box{left:164px;top:714px;width:226px;height:77px;background:var(--red);padding:8px 10px 0 10px;font-size:12.5px;line-height:19px;font-family:'Rubik',sans-serif;color:var(--white)}
</style>
</head>
<body>

<section class="flyer flyer--front">
  <svg class="shapes" viewBox="0 0 390 801" aria-hidden="true">
    <defs>
      <linearGradient id="frontBg" x1="0" y1="0" x2="0" y2="1">
        <stop offset="0" stop-color="#ffffff"/><stop offset="1" stop-color="#e6e6e6"/>
      </linearGradient>
      <linearGradient id="frontRed" x1="0" y1="0" x2="1" y2="1">
        <stop offset="0" stop-color="#b5121a"/><stop offset=".6" stop-color="#d52a22"/><stop offset="1" stop-color="#e6553a"/>
      </linearGradient>
    </defs>
    <rect width="390" height="801" fill="url(#frontBg)"/>
    <path d="M0 150 Q200 152 390 108 L390 126 Q200 176 0 176 Z" fill="#4a4a4a"/>
    <path d="M0 170 Q210 168 390 120 L390 370 Q230 320 0 335 Z" fill="url(#frontRed)" role="img" aria-label="Business handshake photo with red tint"/>
    <path d="M0 335 Q240 318 390 372 L390 470 Q250 340 0 350 Z" fill="#4a4a4a"/>
    <path d="M0 712 Q200 698 390 726 L390 740 Q200 714 0 726 Z" fill="var(--red)"/>
    <path d="M0 724 Q200 712 390 738 L390 770 L0 770 Z" fill="var(--charcoal)"/>
    <rect y="770" width="390" height="31" fill="var(--red)"/>
  </svg>

  <div class="abs brand brand--front"><span class="brand__mark"></span>Ledgerwise</div>

  <h1 class="abs headline">EVERYTHING<br>YOU NEED FROM<br>AN ACCOUNTANT</h1>

  <div class="abs why"><div class="why__lead">WHY CHOOSE</div><div class="why__name">LEDGERWISE?</div></div>

  <ul class="abs benefits">
    <li><svg viewBox="0 0 15 14"><path d="M1 7 L5.5 12 L14 1.5" fill="none" stroke="#c8161d" stroke-width="2.6"/></svg>Value for money</li>
    <li><svg viewBox="0 0 15 14"><path d="M1 7 L5.5 12 L14 1.5" fill="none" stroke="#c8161d" stroke-width="2.6"/></svg>Mobile visits to your farm or business</li>
    <li><svg viewBox="0 0 15 14"><path d="M1 7 L5.5 12 L14 1.5" fill="none" stroke="#c8161d" stroke-width="2.6"/></svg>Fixed Fees Agreed Upfront</li>
    <li><svg viewBox="0 0 15 14"><path d="M1 7 L5.5 12 L14 1.5" fill="none" stroke="#c8161d" stroke-width="2.6"/></svg>Advice tailored to your circumstances</li>
    <li><svg viewBox="0 0 15 14"><path d="M1 7 L5.5 12 L14 1.5" fill="none" stroke="#c8161d" stroke-width="2.6"/></svg>Help to grow your business</li>
    <li><svg viewBox="0 0 15 14"><path d="M1 7 L5.5 12 L14 1.5" fill="none" stroke="#c8161d" stroke-width="2.6"/></svg>Talk directly to your accountant, the person<br>who knows you</li>
    <li><svg viewBox="0 0 15 14"><path d="M1 7 L5.5 12 L14 1.5" fill="none" stroke="#c8161d" stroke-width="2.6"/></svg>Small business &amp; Primary Producer Specialists</li>
  </ul>

  <p class="abs slogan"><span class="slogan__name">LEDGERWISE</span><span class="slogan__line">YOU'RE MORE THAN A FILE</span><span class="slogan__line">TO US</span></p>

  <div class="abs portrait portrait--front" role="img" aria-label="Portrait photo of the director"></div>

  <div class="abs contact contact--front">
    <div class="contact__row"><svg class="icon" viewBox="0 0 12 12"><circle cx="6" cy="6" r="5.2" fill="none" stroke="#fff"/><path d="M4 3.3 L5 3.3 L5.4 5 L4.8 5.5 Q5.5 7 6.6 7.3 L7.1 6.7 L8.7 7.1 L8.7 8.2 Q5 8.5 3.8 4 Z" fill="#fff"/></svg>(07) 4619 2235</div>
    <div class="contact__row"><svg class="icon" viewBox="0 0 12 12"><path d="M6 11 L2.8 6.2 A3.6 3.6 0 1 1 9.2 6.2 Z" fill="#fff"/><circle cx="6" cy="4.4" r="1.3" fill="#3d3d3d"/></svg>PO Box 716 Tarrawong Qld 4417</div>
  </div>
  <div class="abs divider"></div>
  <div class="abs staff">Director: Peter Dunmore CPA<br>Associate: Belinda Vasey CPA</div>

  <div class="abs web--front"><svg class="icon" viewBox="0 0 12 12"><circle cx="6" cy="6" r="5" fill="none" stroke="#fff"/><ellipse cx="6" cy="6" rx="2.2" ry="5" fill="none" stroke="#fff"/><path d="M1 6 H11" stroke="#fff"/></svg>www.ledgerwise.com.au</div>
</section>

<section class="flyer flyer--back">
  <svg class="shapes" viewBox="0 0 390 801" aria-hidden="true">
    <defs>
      <linearGradient id="backBg" x1="0" y1="0" x2="0" y2="1">
        <stop offset="0" stop-color="#ffffff"/><stop offset="1" stop-color="#e8e8e8"/>
      </linearGradient>
    </defs>
    <rect width="390" height="801" fill="url(#backBg)"/>
  </svg>
  <div class="abs photo--back" role="img" aria-label="Photo of a business handshake in front of glass office towers"></div>
  <svg class="shapes" viewBox="0 0 390 801" aria-hidden="true">
    <path d="M0 205 Q190 250 390 230 L390 262 Q200 268 0 240 Z" fill="#ffffff"/>
    <path d="M0 214 Q190 258 390 238 L390 320 Q200 330 0 390 Z" fill="var(--red)"/>
    <path d="M0 390 Q200 330 390 320 L390 332 Q200 346 0 402 Z" fill="#5a5a5a"/>
    <path d="M0 402 Q200 346 390 332 L390 340 Q200 356 0 412 Z" fill="#ffffff"/>
  </svg>

  <div class="abs badge">
    <div class="badge__name">Ledgerwise</div>
    <div class="badge__meta">BN: 41 208 557 190<br>Tax Agent: 6093 1184</div>
  </div>

  <div class="abs portrait portrait--back" role="img" aria-label="Portrait photo of the director"></div>

  <div class="abs about">
    <p>Ledgerwise is a small boutique accounting and auditing practice owned and operated by Peter Dunmore CPA. Peter has been working in commercial accounting and the public accounting and auditing industry for more than 20 years, Peter has previously held Partnership and Principal positions at Brennan &amp; Co Accountants, Hollis Brennan Accountants and Westvale Audit Services.</p>
    <p>During this time Peter has developed a practical, whole of business approach specialising in personalised service to his clients. Peter is the first point of contact when his clients are seeking advice in relation to any aspect of their business.</p>
    <p>At Ledgerwise we are focused on two things, you and your business. We will always put our clients interests first and foremost in every situation.</p>
    <p>If you are looking for a personalised service for you and your business - call us on 07 4619 2235 or 0412 738 206 and experience the difference today</p>
  </div>

  <div class="abs brand brand--back"><span class="brand__mark"></span>Ledgerwise</div>

  <div class="abs contact-box">
    <div class="contact__row"><svg class="icon" viewBox="0 0 12 12"><circle cx="6" cy="6" r="5.2" fill="none" stroke="#fff"/><path d="M4 3.3 L5 3.3 L5.4 5 L4.8 5.5 Q5.5 7 6.6 7.3 L7.1 6.7 L8.7 7.1 L8.7 8.2 Q5 8.5 3.8 4 Z" fill="#fff"/></svg>Call (07) 4619 2235</div>
    <div class="contact__row"><svg class="icon" viewBox="0 0 12 12"><circle cx="6" cy="6" r="5" fill="none" stroke="#fff"/><ellipse cx="6" cy="6" rx="2.2" ry="5" fill="none" stroke="#fff"/><path d="M1 6 H11" stroke="#fff"/></svg>www.ledgerwise.com.au</div>
    <div class="contact__row"><svg class="icon" viewBox="0 0 12 12"><path d="M6 11 L2.8 6.2 A3.6 3.6 0 1 1 9.2 6.2 Z" fill="#fff"/><circle cx="6" cy="4.4" r="1.3" fill="#c8161d"/></svg>PO Box 716 Tarrawong Qld 4417</div>
  </div>
</section>

</body>
</html>
```